Harlow Crest Holdings (Remodeling company) needs a logo and business card

We need a business card design for a new company. We "flip" upmarket houses (buy, remodel and sell) in the Austin, TX area. I'd like neutral colors (grey, white, gold black). I would like it to include a simple, clean logo. Our designs are modern and uncluttered and I would like that reflected in the business card design.

Target Market(s)

Young professionals, Families, Retirees. Our properties will sell for $750k+

Industry/Entity Type

Real Estate

Contact Information for Business Card

Harlow Crest Holdings
Mona Harlow
(979) 555 0142
Owner
Rolf Tandem
(512) 555 0176
Realtor

Logo Text

Harlow Crest Holdings

Font styles to use
Serif
Script

Requirements
Must have
• Simple, classic design
Nice to have
• Clean lines, modern look
Should not have
• Too traditionally

```html
<!DOCTYPE html>
<html lang="en">
<head>
<meta charset="utf-8">
<title>Harlow Crest Holdings – Business Card</title>
<link rel="stylesheet" href="https://fonts.googleapis.com/css2?family=Michroma&family=Roboto+Condensed:wght@400&display=swap">
<style>
  :root {
    --backdrop: #a8a6a7;
    --card: #0d0d0d;
    --card-glow: #1c1c1c;
    --white: #ffffff;
    --soft-grey: #cfcfcf;
    --rule: #4a4a4a;
    --gold: #d9a441;
  }
  * { margin: 0; padding: 0; box-sizing: border-box; }
  html, body { width: 1200px; height: 1200px; overflow: hidden; }
  body { background: var(--backdrop); position: relative; font-family: "Roboto Condensed", sans-serif; }

  .card {
    position: absolute;
    width: 712px;
    height: 418px;
    border-radius: 24px;
    background: var(--card);
    overflow: hidden;
  }
  .card--front { left: 238px; top: 118px; }
  .card--back  { left: 231px; top: 643px; }

  .card__interior {
    position: absolute; inset: 0;
    background:
      radial-gradient(ellipse at 70% 40%, #262320 0%, rgba(20,20,20,0) 55%),
      linear-gradient(160deg, var(--card-glow) 0%, var(--card) 70%);
  }

  .wordmark {
    position: absolute;
    display: flex;
    flex-direction: column;
    align-items: center;
    font-family: "Michroma", sans-serif;
    font-weight: 400;
    color: var(--white);
    text-align: center;
    line-height: 1.2;
    white-space: nowrap;
  }
  .wordmark__square {
    width: 14px; height: 14px;
    background: var(--white);
    margin-bottom: 16px;
  }
  .card--front .wordmark { left: 0; right: 0; top: 150px; font-size: 44px; }
  .card--front .wordmark__sub { font-size: 22px; margin-top: 4px; }
  .card--back .wordmark { left: 26px; width: 340px; top: 160px; font-size: 30px; }
  .card--back .wordmark__square { width: 11px; height: 11px; margin-bottom: 12px; }
  .card--back .wordmark__sub { font-size: 16px; margin-top: 3px; }
  .wordmark__line { display: block; }

  .divider {
    position: absolute; left: 386px; top: 126px;
    width: 1px; height: 170px; background: var(--rule);
  }

  .contact { position: absolute; left: 413px; top: 132px; color: var(--white); }
  .contact__name { font-family: "Michroma", sans-serif; font-size: 21px; letter-spacing: 0.3px; }
  .contact__role { font-size: 15px; color: var(--soft-grey); margin-top: 4px; }
  .contact__list { list-style: none; margin-top: 16px; }
  .contact__item { display: flex; align-items: center; font-size: 17px; height: 29px; }
  .contact__icon { width: 16px; height: 16px; margin-right: 20px; fill: var(--gold); }
</style>
</head>
<body>

<section class="card card--front">
  <div class="card__interior" role="img" aria-label="Dim photograph of a dark, modern furnished interior"></div>
  <div class="wordmark">
    <span class="wordmark__square"></span>
    <span class="wordmark__line">Harlow Crest</span>
    <span class="wordmark__line wordmark__sub">Holdings</span>
  </div>
</section>

<section class="card card--back">
  <div class="card__interior" role="img" aria-label="Dim photograph of a dark, modern furnished interior"></div>
  <div class="wordmark">
    <span class="wordmark__square"></span>
    <span class="wordmark__line">Harlow Crest</span>
    <span class="wordmark__line wordmark__sub">Holdings</span>
  </div>
  <div class="divider"></div>
  <div class="contact">
    <p class="contact__name">Mona Harlow</p>
    <p class="contact__role">Owner</p>
    <ul class="contact__list">
      <li class="contact__item">
        <svg class="contact__icon" viewBox="0 0 16 16"><path d="M2 6c0-2 2-3 6-3s6 1 6 3v1h-3V5.5H5V7H2z"/><rect x="3" y="8" width="10" height="6" rx="1"/></svg>
        (979) 555 0142
      </li>
      <li class="contact__item">
        <svg class="contact__icon" viewBox="0 0 16 16"><rect x="1" y="3" width="14" height="10"/><path d="M1 3l7 6 7-6" fill="none" stroke="#0d0d0d" stroke-width="1.4"/></svg>
        mona@harlowcrestholdings.com
      </li>
      <li class="contact__item">
        <svg class="contact__icon" viewBox="0 0 16 16"><circle cx="8" cy="8" r="7"/><path d="M1 8h14M8 1c-3 3-3 11 0 14M8 1c3 3 3 11 0 14" fill="none" stroke="#0d0d0d" stroke-width="1"/></svg>
        www.harlowcrestholdings.com
      </li>
    </ul>
  </div>
</section>

</body>
</html>
```